Business card for medical clinic

I need an upmarket, modern medical/health business card for my clinic

Contact Information for Business Card

name, address, email, qr code

```html
<!DOCTYPE html>
<html lang="en">
<head>
<meta charset="utf-8">
<title>Calden Health Group – Business Card</title>
<link href="https://fonts.googleapis.com/css2?family=Inter:wght@300;400&family=Source+Sans+3:wght@500;600&display=swap" rel="stylesheet">
<style>
  :root {
    --page: #ffffff;
    --navy: #0a2550;
    --brand-blue: #0d72c9;
    --name-blue: #1b78cf;
    --back-bg: #fbfbfb;
    --frame: #1e5aa8;
    --ink: #0c2a5a;
    --mark: #1a3c6e;
    --sky: #2a9ee0;
  }
  * { margin: 0; padding: 0; box-sizing: border-box; }
  html, body {
    width: 1054px;
    height: 1200px;
    overflow: hidden;
    background: var(--page);
  }
  .canvas { position: relative; width: 1054px; height: 1200px; }

  .card {
    position: absolute;
    left: 148px;
    width: 732px;
    height: 457px;
    overflow: hidden;
  }

  /* Front */
  .card-front { top: 133px; background: var(--navy); }
  .band {
    position: absolute;
    left: 0;
    width: 340px;
    height: 18px;
    background: var(--brand-blue);
  }
  .band-top { top: 0; }
  .band-bottom { bottom: 0; }
  .accent {
    position: absolute;
    left: 340px;
    width: 196px;
    height: 126px;
  }
  .accent-top {
    top: 0;
    background: linear-gradient(160deg, rgba(13,114,201,0.85) 0%, rgba(13,114,201,0.25) 60%, rgba(10,37,80,0) 100%);
  }
  .accent-bottom {
    bottom: 0;
    background: linear-gradient(20deg, rgba(13,114,201,0.85) 0%, rgba(13,114,201,0.25) 60%, rgba(10,37,80,0) 100%);
  }
  .front-name {
    position: absolute;
    left: 0; right: 0;
    top: 188px;
    text-align: center;
    color: #ffffff;
    font-family: "Source Sans 3", sans-serif;
    font-weight: 600;
    line-height: 1.15;
  }
  .front-name .line-main { display: block; font-size: 52px; letter-spacing: 2px; }
  .front-name .line-sub { display: block; font-size: 21px; letter-spacing: 11px; margin-right: -11px; }

  /* Back */
  .card-back {
    top: 608px;
    background: var(--back-bg);
    border: 2px solid var(--frame);
  }
  .holder {
    position: absolute;
    right: 78px;
    top: 52px;
    text-align: right;
  }
  .holder-name {
    font-family: "Inter", sans-serif;
    font-weight: 300;
    font-size: 52px;
    color: var(--name-blue);
    letter-spacing: 0.5px;
    line-height: 1;
  }
  .holder-role {
    margin-top: 6px;
    font-family: "Inter", sans-serif;
    font-weight: 400;
    font-size: 17px;
    letter-spacing: 21px;
    margin-right: -21px;
    color: var(--name-blue);
  }

  .contacts { position: absolute; left: 379px; top: 0; list-style: none; }
  .contact {
    position: absolute;
    left: 0;
    display: flex;
    align-items: center;
    gap: 20px;
    white-space: nowrap;
    font-family: "Source Sans 3", sans-serif;
    font-weight: 500;
    font-size: 19px;
    color: var(--ink);
  }
  .contact-phone   { top: 160px; }
  .contact-mail    { top: 218px; }
  .contact-address { top: 274px; }
  .contact-web     { top: 333px; }
  .contact-icon {
    width: 35px; height: 35px;
    border-radius: 50%;
    background: var(--ink);
    display: flex; align-items: center; justify-content: center;
    flex: none;
  }
  .contact-icon svg { width: 16px; height: 16px; fill: #ffffff; }

  .back-brand {
    position: absolute;
    left: 48px;
    top: 276px;
    display: flex;
    align-items: center;
    gap: 14px;
  }
  .brand-dot {
    width: 40px; height: 40px;
    border-radius: 50%;
    background: var(--sky);
    flex: none;
  }
  .brand-name {
    font-family: "Source Sans 3", sans-serif;
    font-weight: 600;
    color: var(--mark);
    line-height: 1.1;
  }
  .brand-name .line-main { display: block; font-size: 26px; letter-spacing: 1px; }
  .brand-name .line-sub { display: block; font-size: 13px; letter-spacing: 6px; }
</style>
</head>
<body>
<div class="canvas">

  <section class="card card-front" aria-label="Card front">
    <div class="band band-top"></div>
    <div class="band band-bottom"></div>
    <div class="accent accent-top" role="img" aria-label="Blue curved accent decoration"></div>
    <div class="accent accent-bottom" role="img" aria-label="Blue curved accent decoration"></div>
    <h1 class="front-name">
      <span class="line-main">CALDEN HEALTH</span>
      <span class="line-sub">GROUP</span>
    </h1>
  </section>

  <section class="card card-back" aria-label="Card back">
    <div class="holder">
      <p class="holder-name">JHON DOE</p>
      <p class="holder-role">OWNER</p>
    </div>

    <ul class="contacts">
      <li class="contact contact-phone">
        <span class="contact-icon"><svg viewBox="0 0 24 24"><path d="M6.6 10.8a15.1 15.1 0 0 0 6.6 6.6l2.2-2.2a1 1 0 0 1 1-.25 11.4 11.4 0 0 0 3.6.57 1 1 0 0 1 1 1V20a1 1 0 0 1-1 1A17 17 0 0 1 3 4a1 1 0 0 1 1-1h3.5a1 1 0 0 1 1 1c0 1.250.2 2.450.57 3.57a1 1 0 0 1-.25 1z"/></svg></span>
        +123 456 789
      </li>
      <li class="contact contact-mail">
        <span class="contact-icon"><svg viewBox="0 0 24 24"><path d="M3 5h18a1 1 0 0 1 1 1v12a1 1 0 0 1-1 1H3a1 1 0 0 1-1-1V6a1 1 0 0 1 1-1zm9 7.2L4.2 7v.1L12 13l7.8-5.9V7z"/></svg></span>
        mail@mail.com
      </li>
      <li class="contact contact-address">
        <span class="contact-icon"><svg viewBox="0 0 24 24"><path d="M12 2a7 7 0 0 0-7 7c0 5.2 7 13 7 13s7-7.8 7-13a7 7 0 0 0-7-7zm0 9.5A2.5 2.5 0 1 1 12 6.5a2.5 2.5 0 0 1 0 5z"/></svg></span>
        123 Lorem ipsum dolor.
      </li>
      <li class="contact contact-web">
        <span class="contact-icon"><svg viewBox="0 0 24 24"><path d="M12 2a10 10 0 1 0 0 20 10 10 0 0 0 0-20zm6.9 6h-2.9a15 15 0 0 0-1.4-3.6A8 8 0 0 1 18.9 8zM12 4c.8 1.2 1.5 2.5 1.9 4h-3.8c.4-1.5 1.1-2.8 1.9-4zM4.3 14a8 8 0 0 1 0-4h3.4a16 16 0 0 0 0 4zm.8 2h2.9c.3 1.3.8 2.5 1.4 3.6A8 8 0 0 1 5.1 16zM8 8H5.1a8 8 0 0 1 4.3-3.6C8.8 5.5 8.3 6.7 8 8zm4 12c-.8-1.2-1.5-2.5-1.9-4h3.8c-.4 1.5-1.1 2.8-1.9 4zm2.3-6H9.7a14 14 0 0 1 0-4h4.6a14 14 0 0 1 0 4zm.3 5.6c.6-1.100 1.1-2.300 1.4-3.6h2.9a8 8 0 0 1-4.3 3.6zM16.3 14a16 16 0 0 0 0-4h3.4a8 8 0 0 1 0 4z"/></svg></span>
        www.web.com
      </li>
    </ul>

    <div class="back-brand">
      <span class="brand-dot" aria-hidden="true"></span>
      <p class="brand-name">
        <span class="line-main">CALDEN HEALTH</span>
        <span class="line-sub">GROUP</span>
      </p>
    </div>
  </section>

</div>
</body>
</html>
```